Harborline Motors LLC

Car Dealer Customer Service
Address: 2741 Linden Avenue, Cedarbrook, WA 98999
web: www.harborlinemotorsus.net
email: harborlinemotorsus@mailbox-example.net
Phone: (555) 555-0148
Phone: (555) 555-0173

```html
<!DOCTYPE html>
<html lang="en">
<head>
<meta charset="utf-8">
<title>Harborline Motors – Business Card</title>
<link rel="stylesheet" href="https://fonts.googleapis.com/css2?family=Montserrat:wght@700;800&family=Josefin+Sans:wght@400;600&display=swap">
<style>
  :root {
    --brand-blue: #2a8fc9;
    --brand-yellow: #f2b035;
    --ink: #3a3a3a;
    --paper: #ffffff;
    --stage: #e9ecef;
  }
  * { box-sizing: border-box; margin: 0; padding: 0; }
  html, body {
    width: 1200px; height: 800px; overflow: hidden;
    background: var(--stage);
  }
  .stage {
    width: 1200px; height: 800px;
    display: flex; align-items: center; justify-content: center; gap: 50px;
  }
  .card {
    position: relative;
    width: 540px; height: 309px;
    border-radius: 4px;
    overflow: hidden;
    box-shadow: 0 10px 24px rgba(0,0,0,.18);
  }
  /* Front */
  .card-front {
    background:
      radial-gradient(circle at 0% 10%, rgba(246,170,210,.55), transparent 45%),
      radial-gradient(circle at 45% 0%, rgba(255,240,160,.6), transparent 45%),
      radial-gradient(circle at 100% 25%, rgba(150,220,240,.6), transparent 50%),
      var(--paper);
  }
  .brand {
    position: absolute; left: 30px; top: 112px;
    width: 220px;
    display: flex; flex-direction: column; align-items: center; gap: 12px;
  }
  .brand-dot {
    width: 62px; height: 62px; border-radius: 50%;
    background: var(--brand-yellow);
  }
  .brand-name {
    font-family: "Montserrat", sans-serif; font-weight: 800;
    font-size: 22px; letter-spacing: .5px; line-height: 1.1;
    color: var(--brand-blue); text-transform: uppercase; text-align: center;
  }
  .contact {
    position: absolute; left: 258px; top: 32px; width: 272px;
    font-family: "Josefin Sans", sans-serif; color: var(--ink);
  }
  .contact-title {
    font-family: "Montserrat", sans-serif; font-weight: 700;
    font-size: 12px; color: var(--brand-blue); text-transform: uppercase;
    padding-bottom: 4px; border-bottom: 2px solid var(--brand-yellow);
    display: inline-block; margin-bottom: 10px;
  }
  .contact-list { list-style: none; display: flex; flex-direction: column; gap: 5px; }
  .contact-item {
    display: flex; align-items: flex-start; gap: 7px;
    font-size: 13px; line-height: 1.25; white-space: nowrap;
  }
  .contact-item--email { font-size: 12.5px; letter-spacing: -.1px; }
  .contact-icon { flex: 0 0 16px; width: 16px; height: 16px; margin-top: 1px; }
  .card-footer { position: absolute; left: 0; bottom: 0; width: 540px; height: 90px; }
  /* Back */
  .card-back {
    background: var(--brand-blue);
    display: flex; align-items: center; justify-content: center; gap: 16px;
  }
  .card-back .brand-dot { width: 70px; height: 70px; }
  .card-back .brand-name { color: var(--paper); font-size: 26px; text-align: left; }
</style>
</head>
<body>
<main class="stage">
  <section class="card card-front" aria-label="Business card front">
    <div class="brand">
      <span class="brand-dot" aria-hidden="true"></span>
      <span class="brand-name">Harborline Motors</span>
    </div>

    <div class="contact">
      <h2 class="contact-title">Car Dealer Customer Service</h2>
      <ul class="contact-list">
        <li class="contact-item">
          <svg class="contact-icon" viewBox="0 0 16 16" aria-hidden="true"><circle cx="8" cy="8" r="8" fill="var(--brand-yellow)"/><path d="M8 3.5a3 3 0 0 0-3 3c0 2.2 3 5.5 3 5.5s3-3.3 3-5.5a3 3 0 0 0-3-3z" fill="#fff"/><circle cx="8" cy="6.5" r="1.1" fill="var(--brand-yellow)"/></svg>
          <span>2741 Linden Avenue<br>Cedarbrook, WA 98999</span>
        </li>
        <li class="contact-item">
          <svg class="contact-icon" viewBox="0 0 16 16" aria-hidden="true"><circle cx="8" cy="8" r="8" fill="var(--brand-yellow)"/><path d="M5 4l6.5 3.2-2.8.9 1.8 3-1 .6-1.8-3-2 2z" fill="#fff"/></svg>
          <span>www.harborlinemotorsus.net</span>
        </li>
        <li class="contact-item contact-item--email">
          <svg class="contact-icon" viewBox="0 0 16 16" aria-hidden="true"><circle cx="8" cy="8" r="8" fill="var(--brand-yellow)"/><rect x="4" y="5.2" width="8" height="5.6" rx=".6" fill="#fff"/><path d="M4.3 5.6L8 8.4l3.7-2.8" stroke="var(--brand-yellow)" stroke-width=".9" fill="none"/></svg>
          <span>harborlinemotorsus@mailbox-example.net</span>
        </li>
        <li class="contact-item">
          <svg class="contact-icon" viewBox="0 0 16 16" aria-hidden="true"><circle cx="8" cy="8" r="8" fill="var(--brand-yellow)"/><path d="M5.4 4.2l1.5-.3.8 2-1 .8a5 5 0 0 0 2.6 2.6l.8-1 2 .8-.3 1.5c-3.8.4-6.8-2.6-6.4-6.4z" fill="#fff"/></svg>
          <span>(555) 555-0148<br>(555) 555-0173</span>
        </li>
      </ul>
    </div>

    <svg class="card-footer" viewBox="0 0 540 90" preserveAspectRatio="none" aria-hidden="true">
      <path d="M0 68 L300 60 Q330 58 345 50 L540 40 L540 90 L0 90 Z" fill="var(--brand-blue)"/>
      <path d="M310 54 Q330 20 380 18 L540 0 L540 40 L345 50 Q325 52 310 54 Z" fill="var(--brand-yellow)"/>
    </svg>
  </section>

  <section class="card card-back" aria-label="Business card back">
    <span class="brand-dot" aria-hidden="true"></span>
    <span class="brand-name">Harborline<br>Motors</span>
  </section>
</main>
</body>
</html>
```